Looking for a clean, modern, and professional business card design that reflects Valtrin Systems

The design should include the company logo, contact details, and align with our brand identity. Please use a sophisticated and minimalist style, incorporating [specific colors, if applicable]. Creativity is welcome, but the card must maintain a polished and professional appearance.

Details to Include:

Name: Lou Marchetti
Title: VP Sales / Operations
Company: Valtrin Systems
Phone: 304.617.2285
Email: lou@valtrinsystems.example
Website: www.valtrinsystems.example

```html
<!DOCTYPE html>
<html lang="en">
<head>
<meta charset="utf-8">
<title>Valtrin Systems – Business Card</title>
<link rel="stylesheet" href="https://fonts.googleapis.com/css2?family=Montserrat:wght@600;700&family=Lato:wght@400&display=swap">
<style>
  :root {
    --stage: #1d1e20;
    --card-white: #ffffff;
    --card-black: #232325;
    --ink: #1b1b1d;
    --ink-soft: #6b6b6e;
    --brand-blue: #2f6db5;
    --pattern-grey: #f0f0f0;
    --rule: #8a8a8c;
  }
  * { box-sizing: border-box; margin: 0; padding: 0; }
  html, body { width: 1200px; height: 952px; overflow: hidden; }
  body {
    background: var(--stage);
    display: flex;
    flex-direction: column;
    align-items: center;
    justify-content: center;
    gap: 64px;
  }
  .card {
    position: relative;
    width: 560px;
    height: 320px;
    box-shadow: 0 14px 30px rgba(0,0,0,.45);
    overflow: hidden;
  }
  .card--front { background: var(--card-white); }
  .card--back {
    background: var(--card-black);
    display: flex;
    align-items: center;
    justify-content: center;
  }
  .wordmark {
    display: flex;
    align-items: center;
    gap: 10px;
    font-family: "Montserrat", sans-serif;
    font-weight: 700;
    letter-spacing: 2px;
    text-transform: uppercase;
  }
  .wordmark__square {
    width: 14px; height: 14px;
    background: var(--brand-blue);
  }
  .card--front .wordmark {
    position: absolute;
    left: 40px; top: 38px;
    font-size: 22px;
    color: var(--ink);
  }
  .card--back .wordmark {
    font-size: 30px;
    color: #ffffff;
  }
  .contact {
    position: absolute;
    left: 40px; top: 112px;
    list-style: none;
    font-family: "Lato", sans-serif;
    font-size: 12.5px;
    color: var(--ink-soft);
  }
  .contact__item {
    display: flex;
    align-items: center;
    gap: 9px;
    margin-bottom: 8px;
  }
  .contact__icon {
    width: 16px; height: 16px;
    background: var(--ink);
    border-radius: 3px;
    display: flex; align-items: center; justify-content: center;
  }
  .contact__icon svg { width: 10px; height: 10px; fill: #fff; }
  .identity {
    position: absolute;
    right: 40px; top: 110px;
    text-align: right;
  }
  .identity__name {
    font-family: "Montserrat", sans-serif;
    font-weight: 600;
    font-size: 22px;
    letter-spacing: 1px;
    text-transform: uppercase;
    color: var(--ink);
  }
  .identity__surname { color: var(--brand-blue); font-weight: 700; }
  .identity__title {
    font-family: "Lato", sans-serif;
    font-size: 13px;
    color: var(--ink-soft);
    margin-top: 4px;
  }
  .identity__rule {
    width: 86px; height: 1px;
    background: var(--rule);
    margin: 8px 0 0 auto;
  }
  .backdrop-motif {
    position: absolute;
    left: 40px; bottom: 0;
    width: 300px; height: 110px;
    background: linear-gradient(90deg, var(--pattern-grey), #f6f6f6);
  }
</style>
</head>
<body>
  <section class="card card--front" aria-label="Business card front">
    <div class="wordmark"><span class="wordmark__square"></span>Valtrin Systems</div>

    <ul class="contact">
      <li class="contact__item">
        <span class="contact__icon"><svg viewBox="0 0 10 10"><path d="M2 0.5 L4 2.5 L3 3.6 Q4.2 6 6.4 7 L7.5 6 L9.5 8 L8.2 9.5 Q2.5 8.5 0.5 1.8 Z"/></svg></span>
        304.617.2285
      </li>
      <li class="contact__item">
        <span class="contact__icon"><svg viewBox="0 0 10 10"><path d="M0.5 2 H9.5 V8 H0.5 Z M1.3 2.6 L5 5.4 L8.7 2.6 Z" fill-rule="evenodd"/></svg></span>
        lou@valtrinsystems.example
      </li>
      <li class="contact__item">
        <span class="contact__icon"><svg viewBox="0 0 10 10"><path d="M5 0.5 A4.5 4.5 0 1 0 5 9.5 A4.5 4.5 0 1 0 5 0.5 Z M5 1.6 A3.4 3.4 0 1 1 5 8.4 A3.4 3.4 0 1 1 5 1.6 Z M1.2 4.5 H8.8 V5.5 H1.2 Z" fill-rule="evenodd"/></svg></span>
        www.valtrinsystems.example
      </li>
    </ul>

    <div class="identity">
      <p class="identity__name">Lou <span class="identity__surname">Marchetti</span></p>
      <p class="identity__title">VP Sales / Operations</p>
      <div class="identity__rule"></div>
    </div>

    <div class="backdrop-motif" role="img" aria-label="Faint light-grey brand motif in the lower corner"></div>
  </section>

  <section class="card card--back" aria-label="Business card back">
    <div class="wordmark"><span class="wordmark__square"></span>Valtrin Systems</div>
  </section>
</body>
</html>
```